Alternative Health Practice - Website redesign

With regard to the welcome image, stock photos can't show the faces of other people. And please don't submit a design for a one-page website.
Hello, I am redesigning a website and need some help from a professional.
The old website is here: peter-lindqvist.net (pls note I don't want to reuse the welcome photo from the old site). Much of the written content will remain the same, so note that I also need a page layout/text colour etc that works for text heavy pages: ie www.peter-lindqvist.net/somatic-articles and www.peter-lindqvist.net/client-reviews
My effort at redesigning is underway here: https://pjlindqvist.sitebuildr.net/my-site-7
The original sitebuildr template is this one: https://www.sitebuildr.net/website-template/view/html/2868?originUrl=https%3A%2F%2Fwww.sitebuildr.net%2Fwebsite%2Ftemplates%2Fhtml%2Fhealth-wellness&tpClick=view_button&esi=6305f015-f1b5-4bdd-8dfa-47b7d756bb68
I'm pretty happy with the colour palette. My name Peter Johan Lindqvist is now the "brand" without Rooted Stillness subtitle. Regarding the Welcome section, if you are going to use my photos, it probably needs to be those two that are already there. If you want to put a stock photo there instead, that's fine.
If you want to propose something quite different to my design, I'm happy to receive design files in Photoshop or whatever and then subsequently replicate on Sitebuildr. Up to you.
Target Market(s)
Mostly women, some men ages 28-60.
Coding
Coded - Design and coding required
Number of Pages Required
5+ page
Look and feel
Each slider illustrates characteristics of the customer's brand and the style your logo design should communicate.

```html
<!DOCTYPE html>
<html lang="en">
<head>
<meta charset="utf-8">
<title>Peter Lindqvist – Energy Healing</title>
<link href="https://fonts.googleapis.com/css2?family=Khand:wght@500;600&family=Figtree:wght@400;500;600&display=swap" rel="stylesheet">
<style>
:root{
  --black:#000;
  --ink:#131313;
  --gold:#c9a24a;
  --gold-light:#dcb65a;
  --white:#fff;
  --muted:#e6e6e6;
  --line:#8a7236;
}
*{margin:0;padding:0;box-sizing:border-box}
html,body{width:1200px;height:2508px;overflow:hidden;background:var(--ink)}
body{position:relative;font-family:"Figtree",sans-serif;color:var(--white)}
.abs{position:absolute}
.display{font-family:"Khand",sans-serif;font-weight:600;line-height:1}
.gold{color:var(--gold)}
.btn{position:absolute;display:flex;align-items:center;justify-content:center;background:linear-gradient(180deg,var(--gold-light),#be963f);color:#111;border-radius:30px;font-weight:600;font-size:17px;letter-spacing:.3px;text-transform:uppercase}
.rule{position:absolute;height:2px;background:var(--gold);width:60px}

.hero{position:absolute;left:0;top:0;width:1200px;height:596px;background:var(--black)}
.brand{position:absolute;left:133px;top:40px;display:flex;align-items:center;gap:12px}
.brand .dot{width:30px;height:30px;border-radius:50%;background:var(--gold)}
.brand span{font-size:24px;font-weight:600;letter-spacing:2px;color:var(--white)}
.call{position:absolute;left:756px;top:18px;display:flex;align-items:center;gap:14px}
.icon-circle{width:40px;height:40px;border-radius:50%;background:var(--gold);display:flex;align-items:center;justify-content:center}
.call small{display:block;font-size:14px}
.call strong{display:block;font-size:17px;font-weight:600;letter-spacing:.4px}
.lang{position:absolute;left:1010px;top:38px;font-size:14px;font-weight:600}
.lang .sep{display:inline-block;width:1px;height:16px;background:#888;margin:0 6px;vertical-align:middle}
.nav{position:absolute;top:86px;left:554px;display:flex;gap:35px;font-size:15px}
.nav a{color:var(--white);text-decoration:none}
.nav a.active{color:var(--gold)}
.hero-photo{position:absolute;left:560px;top:116px;width:555px;height:480px;background:radial-gradient(circle at 60% 45%,#5b5a44 0%,#3a3524 40%,#1a150a 75%,#000 100%)}
.hero-title{position:absolute;left:134px;top:243px;font-size:58px}
.hero-title div{height:58px}

.feature-img{position:absolute;left:0;top:684px;width:562px;height:374px;background:linear-gradient(135deg,#d8d2c6 0%,#8a8068 45%,#2b2638 75%,#1c1a2a 100%)}
.para{font-size:14px;line-height:26px;color:var(--muted)}

.card{position:absolute;top:1257px;width:455px;height:201px;border:1px solid var(--line);border-radius:3px}
.avatar{position:absolute;top:-39px;left:20px;width:74px;height:74px;border-radius:50%;border:3px solid #e9e0c8}
.card p{position:absolute;left:23px;top:54px;width:410px}
.card .name{position:absolute;left:23px;top:160px;color:var(--gold);font-size:17px;font-weight:500}
.quote{position:absolute;right:18px;bottom:18px}

.about-img{position:absolute;left:656px;top:1670px;width:412px;height:410px;border-radius:50%;background:radial-gradient(circle,#c08a50 0%,#8b7048 45%,#4a3a26 80%,#131313 100%)}

.footer{position:absolute;left:0;top:2173px;width:1200px;height:335px;background:var(--black)}
.flinks{position:absolute;left:134px;top:58px;font-size:14px;line-height:31.7px}
.flinks .active{color:var(--gold)}
.contact{position:absolute;left:341px;display:flex;gap:14px;font-size:14px;line-height:22px}
.contact .icon-circle{flex:none}
.fbrand{position:absolute;left:827px;top:145px;display:flex;align-items:center;gap:10px}
.fbrand .dot{width:26px;height:26px;border-radius:50%;background:var(--gold)}
.fbrand span{font-size:23px;font-weight:600;letter-spacing:2px}
.social{position:absolute;top:2477px;width:29px;height:29px;border:2px solid var(--gold);background:#2a2415}
</style>
</head>
<body>

<header class="hero">
  <div class="brand"><div class="dot"></div><span>PETER LINDQVIST</span></div>
  <div class="call">
    <div class="icon-circle">
      <svg width="20" height="20" viewBox="0 0 24 24" fill="none" stroke="#fff" stroke-width="1.6"><path d="M5 3h4l2 5-2.5 1.5a11 11 0 0 0 6 6L16 13l5 2v4a2 2 0 0 1-2 2A17 17 0 0 1 3 5a2 2 0 0 1 2-2z"/></svg>
    </div>
    <div><small>Call Us</small><strong>(+351) 91 204 7731</strong></div>
  </div>
  <div class="lang"><span class="gold">EN</span><span class="sep"></span>ES</div>
  <nav class="nav">
    <a class="active" href="#">The Practice</a><a href="#">About Me</a><a href="#">Feedback</a><a href="#">Approach</a><a href="#">Contact Me</a>
  </nav>
  <div class="hero-photo" role="img" aria-label="Portrait photo of the practitioner smiling, over a faint gold leaf motif"></div>
  <h1 class="hero-title display">
    <div class="gold">Providing Rooted</div>
    <div class="gold">Stillness</div>
    <div>Energy Healing</div>
  </h1>
  <a class="btn" style="left:132px;top:437px;width:200px;height:51px">Book a Session</a>
</header>

<section>
  <div class="feature-img" role="img" aria-label="Photo of hands resting on a client's legs during an energy healing session"></div>
  <h2 class="abs display" style="left:597px;top:716px;font-size:54px">ENERGY <span class="gold">HEALING</span></h2>
  <div class="rule" style="left:599px;top:776px"></div>
  <p class="abs para" style="left:599px;top:793px;width:460px">A session typically begins by clarifying your intention or wish. You may be facing physical or emotional challenges or seeking help with another aspect of your life, such as family or relationship problems.</p>
  <p class="abs para" style="left:599px;top:874px;width:460px">With your interest in the work clarified, I will assess how energy is flowing in your body and where there are blockages in the physical structure.</p>
  <a class="btn" style="left:599px;top:968px;width:168px;height:52px">Know More</a>
</section>

<section>
  <h2 class="abs display" style="left:0;width:1200px;text-align:center;top:1143px;font-size:54px">CUSTOMER <span class="gold">EXPERIENCES</span></h2>
  <div class="rule" style="left:570px;top:1204px"></div>

  <article class="card" style="left:132px">
    <div class="avatar" role="img" aria-label="Client portrait" style="background:linear-gradient(160deg,#c9b9a0,#6b4a3a)"></div>
    <p class="para">You have given me a lot of confidence in myself. You are showing me a new way of life. And I've learned that it is possible to handle the physical pain caused by our emotions. I didn't know how to cope with it.  Thank you...</p>
    <div class="name">Lucía Moreno Vidal</div>
    <svg class="quote" width="44" height="36" viewBox="0 0 44 36" fill="#555"><path d="M0 6a6 6 0 0 1 6-6h12v20c0 9-6 14-14 16v-7c4-1 6-4 6-8H0zM24 6a6 6 0 0 1 6-6h12v20c0 9-6 14-14 16v-7c4-1 6-4 6-8h-10z"/></svg>
  </article>

  <article class="card" style="left:612px">
    <div class="avatar" role="img" aria-label="Client portrait" style="left:18px;background:linear-gradient(160deg,#4a7bd0,#d8b890)"></div>
    <p class="para">I discovered Rooted Stillness 2 years ago and it amazes me how it has changed my approach to many aspects of my life.</p>
    <div class="name">Claire Dumesnil</div>
    <svg class="quote" width="44" height="36" viewBox="0 0 44 36" fill="#555"><path d="M0 6a6 6 0 0 1 6-6h12v20c0 9-6 14-14 16v-7c4-1 6-4 6-8H0zM24 6a6 6 0 0 1 6-6h12v20c0 9-6 14-14 16v-7c4-1 6-4 6-8h-10z"/></svg>
  </article>

  <a class="btn" style="left:488px;top:1509px;width:224px;height:52px">View All Feedacks</a>
</section>

<section>
  <h2 class="abs display" style="left:133px;top:1660px;font-size:54px;line-height:62px">ABOUT<br>PETER JOHAN <span class="gold">LINDQVIST</span></h2>
  <div class="abs gold" style="left:138px;top:1778px;font-size:19px;font-weight:600">Rooted Stillness® Teacher</div>
  <div class="rule" style="left:136px;top:1811px"></div>
  <p class="abs para" style="left:133px;top:1830px;width:500px">Growing up in Scotland I had a strong connection with nature &amp; the outdoors. Playing outside with friends, with bikes, ball sports, and later mountaineering and rock climbing, was what most interested me.</p>
  <div class="abs gold" style="left:133px;top:1918px;font-size:18px;font-weight:600">Rooted Stillness Studies:</div>
  <ul class="abs" style="left:134px;top:1948px;list-style:none;font-size:14px;line-height:26px;color:var(--muted)">
    <li>Grounded Self Practice®</li><li>Inner Pattern Mapping</li><li>Deep Field Healing®</li>
  </ul>
  <a class="btn" style="left:132px;top:2034px;width:200px;height:52px">Book a Session</a>
  <div class="about-img" role="img" aria-label="Session photo shown inside a circular frame"></div>
</section>

<footer class="footer">
  <div class="flinks">
    <div class="active">Home</div><div>The Practice</div><div>About Me</div><div>Feedback</div><div>Approach</div><div>Contact Me</div>
  </div>

  <div class="contact" style="top:62px">
    <div class="icon-circle"><svg width="18" height="20" viewBox="0 0 24 24" fill="none" stroke="#fff" stroke-width="1.6"><path d="M12 22s7-7 7-12a7 7 0 0 0-14 0c0 5 7 12 7 12z"/><circle cx="12" cy="10" r="2.5"/></svg></div>
    <div>Rua das Oliveiras 12b<br>Bairro Alto Verde, Lisbon, Portugal, 1200-418</div>
  </div>
  <div class="contact" style="top:132px">
    <div class="icon-circle"><svg width="18" height="18" viewBox="0 0 24 24" fill="none" stroke="#fff" stroke-width="1.6"><path d="M5 3h4l2 5-2.5 1.5a11 11 0 0 0 6 6L16 13l5 2v4a2 2 0 0 1-2 2A17 17 0 0 1 3 5a2 2 0 0 1 2-2z"/></svg></div>
    <div>Call Us<br>(+351) 91 204 7731</div>
  </div>
  <div class="contact" style="top:200px">
    <div class="icon-circle" style="width:36px;height:36px"><svg width="18" height="18" viewBox="0 0 24 24" fill="none" stroke="#fff" stroke-width="1.6"><rect x="3" y="6" width="18" height="13" rx="1"/><path d="M3 7l9 7 9-7"/></svg></div>
    <div>Email Us<br>hello@peter-lindqvist.net</div>
  </div>

  <div class="fbrand"><div class="dot"></div><span>PETER LINDQVIST</span></div>
  <a class="btn" style="left:867px;top:194px;width:160px;height:42px;font-size:14px">Book a Session</a>

  <div class="abs" style="left:133px;top:274px;width:938px;height:1px;background:#333"></div>
  <div class="abs" style="right:133px;top:297px;font-size:14px">© 2025 Peter Lindqvist. All Rights Reserved.</div>
</footer>
<div class="social" style="left:133px" aria-label="Social link"></div>
<div class="social" style="left:172px" aria-label="Social link"></div>

</body>
</html>
```